Trifold brochure

Need a trifold marketing brochure for my autism therapy for children business . I would be interested in having designs in both English and Spanish if possible!!!!! Website is www.quillmeadowtherapy.com
Address on brochure needs to be 2736 Larkspur Ave W Suite 5
Minneapolis, MN 55719
Updates
Can you update the address on brochure to 2736 Larkspur Ave W Suite 5
Minneapolis, MN 55719
Target Market(s)
Autism therapy for children
Industry/Entity Type
Autism Therapy
Look and feel

```html
<!DOCTYPE html>
<html lang="en">
<head>
<meta charset="utf-8">
<title>Quill Meadow Therapy – Trifold Brochure</title>
<link href="https://fonts.googleapis.com/css2?family=Tinos:wght@700&family=Figtree:wght@400;500;600&display=swap" rel="stylesheet">
<style>
:root{
  --stage:#5b5b5b;
  --blue:#1d5f93;
  --blue-deep:#174f7e;
  --blue-head:#1f5a90;
  --sub-light:#dbe9f5;
  --orange:#e8662f;
  --white:#ffffff;
  --ink:#2b2b2b;
  --serif:"Tinos", "Times New Roman", serif;
  --sans:"Figtree", Arial, sans-serif;
}
*{box-sizing:border-box;margin:0;padding:0}
html,body{width:1200px;height:1200px;overflow:hidden;background:var(--stage)}
.sheet{position:absolute;left:232px;width:736px;height:568px;background:var(--white);overflow:hidden}
.sheet--outside{top:36px}
.sheet--inside{top:616px}
.panel{position:absolute;top:0;height:568px;overflow:hidden}
.p1{left:0;width:249px}
.p2{left:249px;width:241px}
.p3{left:490px;width:246px}
.photo{position:absolute;left:0;width:100%}
.blue{background:var(--blue);color:var(--white)}
.body{font:400 9.3px/12.3px var(--sans);color:var(--ink)}
.blue .body{color:var(--white)}
.sub{display:flex;align-items:center;gap:4px;font:700 11px/14px var(--serif);color:var(--blue-head);margin-bottom:3px;white-space:nowrap}
.blue .sub{color:var(--sub-light)}
.tick{width:8px;height:8px;flex:none}
.h2{font:700 13.5px/16px var(--serif);color:var(--blue-head);margin-bottom:4px}
.blue .h2{color:var(--white)}
.block{position:absolute;left:23px;right:12px}
.center{text-align:center}
.brand{font-family:var(--sans);font-weight:600;letter-spacing:.5px;text-align:center;line-height:1.25}
</style>
</head>
<body>

<section class="sheet sheet--outside">
  <div class="panel p1">
    <div class="photo" role="img" aria-label="Photo of a mother and toddler playing with a colourful shape sorter" style="top:0;height:168px;background:linear-gradient(135deg,#c8c3bd,#e9e4dc 55%,#d8b96a)"></div>
    <div class="block" style="top:176px">
      <div class="sub"><svg class="tick" viewBox="0 0 10 10"><circle cx="5" cy="5" r="4.3" fill="none" stroke="currentColor" stroke-width="1"/><path d="M3 5.2l1.4 1.4L7.2 3.8" fill="none" stroke="currentColor" stroke-width="1"/></svg>Occupational Therapy (OT)</div>
      <p class="body">Occupational therapy at Quill Meadow targets the development of fine motor skills, sensory processing abilities, and self-care capabilities in children with autism. Through engaging activities and individualized interventions, our occupational therapists help children build essential life skills and gain independence in daily activities.</p>
      <div class="sub" style="margin-top:12px"><svg class="tick" viewBox="0 0 10 10"><circle cx="5" cy="5" r="4.3" fill="none" stroke="currentColor" stroke-width="1"/><path d="M3 5.2l1.4 1.4L7.2 3.8" fill="none" stroke="currentColor" stroke-width="1"/></svg>Social Skills Training</div>
      <p class="body">Our social skills training programs focus on teaching crucial social skills to children with autism, enabling them to navigate social interactions confidently. Through structured group activities and personalized coaching, we empower children to build friendships, communicate effectively, and thrive in social settings.</p>
    </div>
    <div class="photo" role="img" aria-label="Photo of a group of children playing with blocks around a small table" style="top:402px;height:166px;background:linear-gradient(135deg,#8a7a66,#d9d3c6 50%,#9aa88c)"></div>
  </div>

  <div class="panel p2 blue" style="background:linear-gradient(160deg,#1f6399,#1a5788)">
    <h1 class="center" style="position:absolute;top:20px;left:8px;right:8px;font:700 25px/27px var(--serif)">Ready to Take<br>the Next Step?</h1>
    <h2 class="center" style="position:absolute;top:100px;left:6px;right:6px;font:700 25px/27px var(--serif)">Contact Us Today<br>for<br>Expert Autism<br>Therapy Services!</h2>
    <p class="body center" style="position:absolute;top:224px;left:22px;right:22px">Contact us today to learn more about our ABA therapy for autism services and how we can help your child thrive.</p>
    <div class="body center" style="position:absolute;top:302px;left:10px;right:10px;line-height:13.2px">
      <p>Monday - Friday | 9 am- 8 pm</p>
      <p>Saturday - Sunday | 9 am-5 pm</p>
      <p style="margin-top:10px"><svg width="8" height="9" viewBox="0 0 8 10"><path d="M4 .6a3 3 0 0 0-3 3c0 2.2 3 5.8 3 5.8s3-3.6 3-5.8a3 3 0 0 0-3-3z" fill="none" stroke="#fff" stroke-width="1"/><circle cx="4" cy="3.6" r="1" fill="#fff"/></svg> 2736 Larkspur Ave W</p>
      <p>Suite 5, Minneapolis, MN 55719,</p>
      <p><svg width="9" height="8" viewBox="0 0 10 8"><rect x=".5" y=".5" width="9" height="7" fill="none" stroke="#fff"/><path d="M.5 .5l4.5 4 4.5-4" fill="none" stroke="#fff"/></svg> info@quillmeadowtherapy.com</p>
      <p><svg width="8" height="8" viewBox="0 0 10 10"><path d="M2 1l2 2-1 1.3a6 6 0 0 0 2.7 2.7L7 6l2 2-1.2 1.4C4.5 9 1 5.5.6 2.2z" fill="none" stroke="#fff"/></svg> 612-555-0148</p>
    </div>
    <div class="brand" style="position:absolute;top:500px;left:0;right:0;font-size:19px;color:var(--white)">QUILL MEADOW<br><span style="font-size:12px">THERAPY</span></div>
  </div>

  <div class="panel p3">
    <div class="brand" style="position:absolute;top:66px;left:0;right:0;font-size:18px;color:var(--blue-deep)">QUILL MEADOW<br><span style="font-size:11.5px">THERAPY</span></div>
    <div class="photo" role="img" aria-label="Photo of a therapist and a young boy working with an abacus and colourful letter blocks" style="top:107px;height:337px;background:linear-gradient(160deg,#d8d4cf,#c9b9a6 45%,#e6e2dc 75%,#d87a6a)"></div>
    <div class="blue" style="position:absolute;top:444px;left:0;right:0;bottom:0">
      <p class="center" style="margin-top:9px;font:700 25px/31px var(--serif)">Building Bridges<br>to Brighter Futures</p>
      <p class="center" style="margin-top:12px;font:700 13px/15px var(--serif)">www.quillmeadowtherapy.com</p>
    </div>
  </div>
</section>

<section class="sheet sheet--inside">
  <div class="panel p1">
    <div style="position:absolute;top:20px;left:21px;width:205px;height:2px;background:var(--orange)"></div>
    <div class="block" style="top:31px;left:21px;right:22px">
      <h2 class="h2">About Us</h2>
      <p class="body">ABA Therapy Applied Behavioral Analysis (ABA) Therapy is endorsed by leading national health experts and major pediatric care associations and has been scientifically proven to be the most effective in helping a child with autism to acquire the necessary skills to reach their full potential. Research has proven that early diagnosis and intervention are key to achieving success, as well as a commitment to the individualized treatment plan developed specifically for your child by one of our expert Clinicians.</p>
      <h2 class="h2" style="margin-top:24px">Quill Meadow Offers</h2>
      <p class="body">A center-based environment, led by highly-trained and credentialed clinicians. Our team of experienced certified behavior analysts and trained behavior technicians work with you and your child to develop individualized treatment plans based on their unique needs. We consider your child’s needs and wants throughout the entire process. Ultimately, we prepare children for succeeding in all aspects of their life.</p>
    </div>
    <div class="photo" role="img" aria-label="Photo of two boys playing with building blocks in a classroom" style="top:376px;height:192px;background:linear-gradient(135deg,#c99a86,#e1d8cf 50%,#3d5d8f)"></div>
  </div>

  <div class="panel p2 blue">
    <div class="photo" role="img" aria-label="Photo of a child holding up a colourful toy made of interlocking blocks" style="top:0;height:200px;background:linear-gradient(180deg,#d9d2cb 0%,#c7b8ab 55%,#1d5f93 100%)"></div>
    <div class="block" style="top:196px;left:14px;right:10px">
      <h2 class="h2">How we do Aba Therapy?</h2>
      <p class="body">At Quill Meadow, our focus is on creating joy in every child’s learning experience. This means from sign-in to circle time to table time, we are facilitating an environment where the child is learning while they are happy, relaxed, and engaged.</p>
      <h2 class="h2" style="margin-top:13px">Our Approach</h2>
      <div class="sub"><svg class="tick" viewBox="0 0 10 10"><circle cx="5" cy="5" r="4.3" fill="none" stroke="currentColor" stroke-width="1"/><path d="M3 5.2l1.4 1.4L7.2 3.8" fill="none" stroke="currentColor" stroke-width="1"/></svg>Early Intervention</div>
      <p class="body">We understand that early intervention is crucial. Our programs focus on early detection, assessment, and intervention to maximize developmental gains during critical periods.</p>
      <div class="sub" style="margin-top:13px"><svg class="tick" viewBox="0 0 10 10"><circle cx="5" cy="5" r="4.3" fill="none" stroke="currentColor" stroke-width="1"/><path d="M3 5.2l1.4 1.4L7.2 3.8" fill="none" stroke="currentColor" stroke-width="1"/></svg>Individualized Treatment Plans</div>
      <p class="body">No two children with autism are alike. Our experienced therapists create personalized treatment plans based on each child’s strengths, challenges, and developmental goals.</p>
      <div class="sub" style="margin-top:13px"><svg class="tick" viewBox="0 0 10 10"><circle cx="5" cy="5" r="4.3" fill="none" stroke="currentColor" stroke-width="1"/><path d="M3 5.2l1.4 1.4L7.2 3.8" fill="none" stroke="currentColor" stroke-width="1"/></svg>Safe and Supportive Environment</div>
      <p class="body">At Quill Meadow, safety is our priority. Our therapy spaces are designed to be calming and sensory-friendly. We create a nurturing environment where children feel comfortable exploring and</p>
    </div>
  </div>

  <div class="panel p3">
    <div class="photo" role="img" aria-label="Photo of a speech therapist and a child practising sounds at a table" style="top:0;height:145px;background:linear-gradient(135deg,#e3e6e8,#cbbfb1 50%,#eef0f1)"></div>
    <div class="blue" style="position:absolute;top:145px;left:0;right:0;height:273px">
      <div class="block" style="top:10px;left:14px;right:8px">
        <h2 class="h2">Our Services</h2>
        <div class="sub"><svg class="tick" viewBox="0 0 10 10"><circle cx="5" cy="5" r="4.3" fill="none" stroke="currentColor" stroke-width="1"/><path d="M3 5.2l1.4 1.4L7.2 3.8" fill="none" stroke="currentColor" stroke-width="1"/></svg>Applied Behavior Analysis (ABA) Therapy</div>
        <p class="body">Our ABA therapy focuses on enhancing communication, social skills, and behavior management in children with autism spectrum disorder (ASD). Through personalized intervention plans, our skilled therapists employ evidence-based techniques to promote positive behavioral changes and maximize developmental progress.</p>
        <div class="sub" style="margin-top:11px"><svg class="tick" viewBox="0 0 10 10"><circle cx="5" cy="5" r="4.3" fill="none" stroke="currentColor" stroke-width="1"/><path d="M3 5.2l1.4 1.4L7.2 3.8" fill="none" stroke="currentColor" stroke-width="1"/></svg>Speech and Language Therapy</div>
        <p class="body">Our speech and language therapy services aim to improve communication, expressive language, and social interaction abilities in children with autism. Using tailored approaches and innovative techniques, our licensed speech-language pathologists work closely with each child to address their unique communication needs and foster meaningful connections.</p>
      </div>
    </div>
    <div class="photo" role="img" aria-label="Photo of a boy and a therapist in a speech session against a blue wall" style="top:418px;height:150px;background:linear-gradient(135deg,#2e5c9a,#3d6bab 55%,#d9c9b8)"></div>
  </div>
</section>

</body>
</html>
```